Looking for a creative label design for our retail coffee bags

We are a coffee manufacturer (coffee roaster) looking to re-brand our retail label for our coffee bags. Our main coffee blend that we sell is our Harborline Velvet Blend. You can use this name when creating the label. We are going for a look that represents our company as a coffee roaster. Please reference our website (www.brindlemugworks.com) and our Facebook page to learn more about our company and to give you more inspiration on creating this design.

Target Market(s)

Retail customers/grocery stores

Industry/Entity Type

Manufacturer

Requirements
Must have
• The size of the label has to be 3" width x 4" height

Logo must be Black
Nice to have
• We currently incorporate a color on our labels for each blend. For example, Harborline Velvet Blend (royal blue), Decaffeinated Blend (red), Breakfast Blend (green), Flavored coffees (gold).

Rustic/vintage style

```html
<!DOCTYPE html>
<html lang="en">
<head>
<meta charset="utf-8">
<title>Brindle Mugworks – Retail Coffee Labels</title>
<link rel="stylesheet" href="https://fonts.googleapis.com/css2?family=Bebas+Neue&family=Oswald:wght@500&family=Cutive+Mono&display=swap">
<style>
  :root {
    --backdrop: #f2f0ec;
    --label-paper: #ffffff;
    --ink: #161616;
    --rule: #b9b9b9;
    --ribbon-velvet: #b8313b;
    --ribbon-breakfast: #35308b;
    --ribbon-decaf: #5e9a2b;
    --leaf-dark: #3f5a2a;
    --leaf-light: #8aa56a;
    --berry: #9c2b2b;
  }
  * { margin: 0; padding: 0; box-sizing: border-box; }
  html, body { width: 1200px; height: 697px; overflow: hidden; }
  body { background: var(--backdrop); position: relative; }

  .label {
    position: absolute;
    top: 243px;
    width: 208px;
    height: 340px;
    background: var(--label-paper);
    box-shadow: 0 1px 3px rgba(0,0,0,0.12);
  }
  .label--velvet { left: 123px; --accent: var(--ribbon-velvet); }
  .label--breakfast { left: 499px; --accent: var(--ribbon-breakfast); }
  .label--decaf { left: 866px; --accent: var(--ribbon-decaf); }

  .ribbon { position: absolute; left: 25px; top: 0; width: 50px; height: 228px; }
  .ribbon path { fill: var(--accent); }

  .ribbon__text {
    position: absolute;
    left: 17px;
    top: 158px;
    width: 66px;
    text-align: center;
    font-family: 'Bebas Neue', sans-serif;
    font-size: 15px;
    line-height: 14px;
    color: #fff;
    background: var(--accent);
    padding: 4px 0 3px;
  }

  .brand-mark {
    position: absolute;
    left: 30px;
    top: 13px;
    width: 88px;
    height: 88px;
    border-radius: 50%;
    background: var(--ink);
    display: flex;
    align-items: center;
    justify-content: center;
    text-align: center;
  }
  .brand-mark__name {
    font-family: 'Bebas Neue', sans-serif;
    font-size: 19px;
    line-height: 18px;
    color: #fff;
  }

  .divider {
    position: absolute;
    left: 117px;
    right: 0;
    top: 88px;
    border-top: 1px solid var(--rule);
  }

  .illustration {
    position: absolute;
    left: 98px;
    top: 92px;
    width: 100px;
    height: 142px;
    border-radius: 45% 50% 40% 55%;
    background: radial-gradient(circle at 45% 70%, var(--berry) 0 14%, transparent 26%),
                radial-gradient(ellipse at 55% 45%, var(--leaf-light) 0%, var(--leaf-dark) 70%, transparent 72%);
    opacity: 0.85;
  }

  .product-name {
    position: absolute;
    left: 0;
    right: 0;
    top: 232px;
    text-align: center;
    font-family: 'Bebas Neue', sans-serif;
    white-space: nowrap;
  }
  .product-name__origin { display: block; font-size: 33px; line-height: 30px; color: var(--ink); }
  .product-name__blend { display: block; font-size: 24px; line-height: 24px; color: var(--accent); }
  .label--velvet .product-name__blend { font-size: 21px; }

  .product-meta {
    position: absolute;
    left: 0;
    right: 0;
    top: 302px;
    text-align: center;
    font-family: 'Cutive Mono', monospace;
    font-size: 7px;
    line-height: 12px;
    color: var(--ink);
  }
</style>
</head>
<body>

  <article class="label label--velvet">
    <svg class="ribbon" viewBox="0 0 50 228" aria-hidden="true"><path d="M0 0H50V228L25 214L0 228Z"/></svg>
    <div class="ribbon__text">Fresh<br>&amp;Finest<br>Roasted</div>
    <div class="brand-mark"><span class="brand-mark__name">Brindle<br>Mugworks</span></div>
    <div class="divider"></div>
    <div class="illustration" role="img" aria-label="Botanical illustration of a coffee branch with leaves and red cherries"></div>
    <h2 class="product-name"><span class="product-name__origin">Colombian</span><span class="product-name__blend">Harborline Velvet Blend</span></h2>
    <p class="product-meta">16 oz &nbsp;|&nbsp; NET WT. 500g<br>www.brindlemugworks.com</p>
  </article>

  <article class="label label--breakfast">
    <svg class="ribbon" viewBox="0 0 50 228" aria-hidden="true"><path d="M0 0H50V228L25 214L0 228Z"/></svg>
    <div class="ribbon__text">Fresh<br>&amp;Finest<br>Roasted</div>
    <div class="brand-mark"><span class="brand-mark__name">Brindle<br>Mugworks</span></div>
    <div class="divider"></div>
    <div class="illustration" role="img" aria-label="Botanical illustration of a coffee branch with leaves and red cherries"></div>
    <h2 class="product-name"><span class="product-name__origin">Colombian</span><span class="product-name__blend">Breakfast Blend</span></h2>
    <p class="product-meta">16 oz &nbsp;|&nbsp; NET WT. 500g<br>www.brindlemugworks.com</p>
  </article>

  <article class="label label--decaf">
    <svg class="ribbon" viewBox="0 0 50 228" aria-hidden="true"><path d="M0 0H50V228L25 214L0 228Z"/></svg>
    <div class="ribbon__text">Fresh<br>&amp;Finest<br>Roasted</div>
    <div class="brand-mark"><span class="brand-mark__name">Brindle<br>Mugworks</span></div>
    <div class="divider"></div>
    <div class="illustration" role="img" aria-label="Botanical illustration of a coffee branch with leaves and red cherries"></div>
    <h2 class="product-name"><span class="product-name__origin">Colombian</span><span class="product-name__blend">Decaffeinated Blend</span></h2>
    <p class="product-meta">16 oz &nbsp;|&nbsp; NET WT. 500g<br>www.brindlemugworks.com</p>
  </article>

</body>
</html>
```